Business card design for upmarket Home Technology design and Installation company

Hello designers, we need a great business card designed.
We need it to convey high tech, and also sophistication .
We work with some of the most affluent people in the world building them home technology systems, and A/V entertainment systems.

Services offered include the following:
Design, sales, installation, and maintenance of

*Home Automation systems
*Distributed / Multi-Room Audio and Video
*High Performance Networks & WiFi
* Lighting and Shade Control
*Home cinema
*Security and CCTV Systems

I have included a copy of our logo to use for your design efforts.

Target Market(s)

Upmarket clients with multi million euro villas.

Industry/Entity Type

Home technology

Contact Information for Business Card

NAME: Derek Halloran ADDRESS: Plaza Brisa Local 42, Port Andratx, 07392 PHONE: +34-602-518-794 EMAIL: DHalloran@VELTRAsmarthomes.com WEB: www.veltrasmarthomes.com

Requirements
Must have
• Our Logo, and our tagline

```html
<!DOCTYPE html>
<html lang="en">
<head>
<meta charset="utf-8">
<title>Veltra Smarter Homes – Business Card</title>
<link rel="stylesheet" href="https://fonts.googleapis.com/css2?family=Montserrat:wght@500;700&family=Open+Sans:wght@400;700&display=swap">
<style>
  :root {
    --backdrop: #c9c9c9;
    --gold-light: #f1dca6;
    --gold-mid: #d2b06a;
    --gold-deep: #b98f3e;
    --gold-ink: #b8913f;
    --white: #ffffff;
    --ink: #1d1d1d;
    --shadow: rgba(0, 0, 0, 0.28);
  }
  * { box-sizing: border-box; margin: 0; padding: 0; }
  html, body { width: 1200px; height: 900px; overflow: hidden; }
  body {
    background: var(--backdrop);
    font-family: "Open Sans", Arial, sans-serif;
    position: relative;
  }
  .card {
    position: absolute;
    left: 250px;
    width: 700px;
    height: 400px;
    border-radius: 36px;
    box-shadow: 0 10px 24px var(--shadow);
    overflow: hidden;
  }
  .card--front {
    top: 40px;
    background: linear-gradient(200deg, var(--gold-light) 0%, var(--gold-mid) 45%, var(--gold-deep) 100%);
    color: var(--white);
  }
  .card--back {
    top: 460px;
    background: var(--white);
    color: var(--ink);
  }

  /* Brand lockup */
  .brand {
    font-family: "Montserrat", Arial, sans-serif;
    font-weight: 500;
    letter-spacing: 14px;
    line-height: 1;
  }
  .card--front .brand {
    position: absolute;
    left: 150px;
    top: 70px;
    font-size: 92px;
    color: var(--white);
  }
  .tagline {
    position: absolute;
    left: 395px;
    top: 170px;
    font-family: "Montserrat", Arial, sans-serif;
    font-weight: 500;
    font-size: 26px;
    letter-spacing: 1px;
  }
  .rule {
    position: absolute;
    left: 150px;
    top: 188px;
    width: 235px;
    height: 1px;
    background: rgba(255, 255, 255, 0.7);
  }

  /* Services */
  .services-title {
    position: absolute;
    left: 60px;
    top: 236px;
    font-weight: 700;
    font-size: 17px;
    letter-spacing: 0.5px;
  }
  .service-list {
    position: absolute;
    top: 268px;
    list-style: none;
    font-size: 17px;
    line-height: 25px;
  }
  .service-list li::before {
    content: "";
    display: inline-block;
    width: 7px;
    height: 7px;
    border-radius: 50%;
    background: var(--white);
    margin-right: 10px;
    vertical-align: middle;
  }
  .service-list--left { left: 60px; }
  .service-list--right { left: 420px; }

  /* Back side */
  .card--back .brand {
    position: absolute;
    left: 60px;
    top: 70px;
    font-size: 80px;
    color: var(--gold-ink);
  }
  .person-name {
    position: absolute;
    left: 60px;
    top: 200px;
    font-family: "Montserrat", Arial, sans-serif;
    font-weight: 700;
    font-size: 32px;
    color: var(--gold-ink);
  }
  .contact-list {
    position: absolute;
    left: 60px;
    top: 262px;
    list-style: none;
    font-size: 20px;
    line-height: 32px;
  }
  .contact-list li { display: flex; align-items: center; gap: 12px; }
  .contact-icon { width: 20px; height: 20px; flex: none; }
  .address {
    position: absolute;
    right: 50px;
    top: 150px;
    font-size: 20px;
    line-height: 28px;
    text-align: left;
  }
</style>
</head>
<body>

<section class="card card--front" aria-label="Card front">
  <div class="brand">VELTRA</div>
  <div class="rule"></div>
  <div class="tagline">Smarter Homes</div>
  <p class="services-title">DESIGN, SALES, INSTALLATION, AND MAINTENANCE OF</p>
  <ul class="service-list service-list--left">
    <li>Home Automation systems</li>
    <li>Distributed / Multi-Room Audio and Video</li>
    <li>High Performance Networks &amp; WiFi</li>
  </ul>
  <ul class="service-list service-list--right">
    <li>Lighting and Shade Control</li>
    <li>Home cinema</li>
    <li>Security and CCTV Systems</li>
  </ul>
</section>

<section class="card card--back" aria-label="Card back">
  <div class="brand">VELTRA</div>
  <p class="address">Plaza Brisa Local 42<br>Port Andratx, 07392</p>
  <p class="person-name">Derek Halloran</p>
  <ul class="contact-list">
    <li>
      <svg class="contact-icon" viewBox="0 0 24 24" aria-hidden="true"><path fill="#b8913f" d="M6.6 10.8a15 15 0 0 0 6.6 6.6l2.2-2.2c.3-.3.7-.4 1-.2 1.1.4 2.3.6 3.6.6.6 0 1 .4 1 1V20c0 .6-.4 1-1 1A17 17 0 0 1 3 4c0-.6.4-1 1-1h3.5c.6 0 1 .4 1 1 0 1.3.2 2.5.6 3.6.1.3 0 .7-.2 1z"/></svg>
      <span>+34-602-518-794</span>
    </li>
    <li>
      <svg class="contact-icon" viewBox="0 0 24 24" aria-hidden="true"><rect x="2" y="5" width="20" height="14" rx="1" fill="#b8913f"/><path d="M2.5 6l9.5 7 9.5-7" fill="none" stroke="#fff" stroke-width="1.6"/></svg>
      <span>DHalloran@VELTRAsmarthomes.com</span>
    </li>
    <li>
      <svg class="contact-icon" viewBox="0 0 24 24" aria-hidden="true"><g fill="none" stroke="#b8913f" stroke-width="1.8"><circle cx="12" cy="12" r="9.5"/><ellipse cx="12" cy="12" rx="4" ry="9.5"/><path d="M2.5 12h19M4 7h16M4 17h16"/></g></svg>
      <span>www.veltrasmarthomes.com</span>
    </li>
  </ul>
</section>

</body>
</html>
```